Bright Mesh Business Card

This is a business card for a printing company but I actually don't have a logo. Just need to typeset the words "Bright Mesh Printing" as the logo. Then add my name "Loretta Vance" + phone number + address

Target Market(s)

ceos and professionals

Industry/Entity Type

printing and manufacturing

Contact Information for Business Card

Bright Mesh Printing/ 4617 calloway st. Alder Vale, NV 91648/ 555-417-3980/ Loretta Vance

Font styles to use
Serif
Other font styles liked:
• a modern font would be nice

Colors
0054AA
0677BA
7BADD7
CADEEF
E8F1F8
0094D4
00A9DD
6FCCEA
C7EBF8
E9F6FB

Requirements
Must have
• company name, number, address
Nice to have
• nice bold feel
Should not have
• nothing in particular

```html
<!DOCTYPE html>
<html lang="en">
<head>
<meta charset="utf-8">
<title>Bright Mesh Printing — Business Card</title>
<link rel="stylesheet" href="https://fonts.googleapis.com/css2?family=IBM+Plex+Serif:wght@400;500;600&display=swap">
<style>
  :root {
    --backdrop: #eeeeec;
    --card-white: #ffffff;
    --brand-blue: #139ed8;
    --ink: #1c1c1c;
    --ink-soft: #3a3a3a;
    --on-blue: #ffffff;
  }
  * { margin: 0; padding: 0; box-sizing: border-box; }
  html, body {
    width: 1200px;
    height: 900px;
    overflow: hidden;
    background: var(--backdrop);
  }
  .canvas {
    width: 1200px;
    height: 900px;
    display: flex;
    align-items: center;
    justify-content: center;
  }
  .business-card {
    width: 980px;
    height: 560px;
    display: flex;
    background: var(--card-white);
    box-shadow: 0 2px 10px rgba(0, 0, 0, 0.08);
    font-family: "IBM Plex Serif", Georgia, serif;
  }
  .brand-band {
    width: 320px;
    flex-shrink: 0;
    background: var(--brand-blue);
    padding: 52px 40px;
  }
  .company-name {
    color: var(--on-blue);
    font-weight: 500;
    font-size: 54px;
    line-height: 1;
    letter-spacing: 0.5px;
  }
  .contact-panel {
    flex: 1;
    display: flex;
    flex-direction: column;
    justify-content: flex-end;
    padding: 0 48px 64px 40px;
  }
  .contact-name {
    color: var(--ink);
    font-weight: 600;
    font-size: 26px;
    line-height: 1.15;
  }
  .contact-phone {
    color: var(--ink-soft);
    font-size: 26px;
    line-height: 1.15;
    margin-bottom: 40px;
  }
  .contact-address {
    color: var(--ink-soft);
    font-size: 26px;
    line-height: 1.15;
    font-style: normal;
  }
</style>
</head>
<body>
  <main class="canvas">
    <article class="business-card">
      <section class="brand-band">
        <h1 class="company-name">Bright<br>Mesh<br>Printing</h1>
      </section>
      <section class="contact-panel">
        <p class="contact-name">Loretta Vance</p>
        <p class="contact-phone">555-417-3980</p>
        <address class="contact-address">4617 calloway st. Alder Vale, NV 91648</address>
      </section>
    </article>
  </main>
</body>
</html>
```